REDESIGN MAIN BANNER IMAGE FOR MARKETING WEBSITE

I feel like my main banner image is too busy but I like it but i want to see other options. www.brightlanepromoworks.biz I want a nice professional clean design that goes with current theme of site. Must look professional and show the variety of incentives we offer but not be overwelming.

My business is called Brightlane Promo Works and I provide businesses around the world with marketing incentives that they can use to create exciting promotions and contest and marketing giveaways to help attract more customers.

I provide a variety of different types of incentives such as Vacation Certificates, Dining Vouchers, Hotel Savings Cards, Smart Watches, Etc. that businesses can use in their marketing efforts.

I want my main banner image to reflect the variety of different categories of incentives... that I offer here: https://www.brightlanepromoworks.biz/incentives

We can use images of certificates or images.....I just want the content to be the same:

CONTENT FOR MAIN BANNER IMAGE:
INCREASE LEADS AND SALES OVERNIGHT

CREATE EXCITING MARKETING PROMOTIONS GIVING AWAY SMART DEVICES, VACATION CERTIFICATES, DINING VOUCHERS AND OTHER INCENTIVES TO YOUR CUSTOMERS

GET A FREE SAMPLE PACKAGE FOR A LIMITED TIME ONLY

Target Market(s)

b2b business owners, ceo, president, owner, founder

Industry/Entity Type

Promotional

Requirements
Must have
• Hi guys keep in mind the finished product will have to be 1800x840

Nice to have
• I want a nice professional clean design that goes with current theme of site. Must look professional and show the variety of incentives we offer but not be overwelming.
Should not have

```html
<!DOCTYPE html>
<html lang="en">
<head>
<meta charset="utf-8">
<title>Brightlane Promo Works – Increase Leads and Sales Overnight</title>
<link rel="stylesheet" href="https://fonts.googleapis.com/css2?family=Montserrat:wght@400;500;600;700;800&display=swap">
<style>
  :root {
    --navy-deep: #073766;
    --navy: #0b4c8c;
    --navy-mid: #0d5ca6;
    --band-blue: #1177cc;
    --band-light: #39b4f5;
    --glow: #5fd3ff;
    --white: #ffffff;
    --green: #4cd85a;
    --green-dark: #2aa82e;
    --tab-top: #ffffff;
    --tab-bottom: #d7dde4;
    --tab-text: #0c3a66;
  }
  * { margin: 0; padding: 0; box-sizing: border-box; }
  html, body { width: 1200px; height: 560px; overflow: hidden; }
  body { font-family: "Montserrat", sans-serif; color: var(--white); }

  .banner {
    position: relative;
    width: 1200px;
    height: 560px;
    overflow: hidden;
    background:
      radial-gradient(ellipse 60% 55% at 45% 40%, var(--navy-mid) 0%, transparent 70%),
      linear-gradient(180deg, var(--navy) 0%, var(--navy-deep) 100%);
  }

  .light-streaks { position: absolute; inset: 0; }

  .headline {
    position: absolute;
    top: 20px;
    left: 0;
    width: 100%;
    text-align: center;
    font-weight: 800;
    font-size: 45px;
    letter-spacing: 0.2px;
    line-height: 54px;
  }
  .headline .accent { color: var(--green); }

  .flyer-stack { position: absolute; left: 0; top: 0; }

  .pitch {
    position: absolute;
    left: 692px;
    top: 128px;
    width: 400px;
    font-weight: 700;
    font-size: 21px;
    line-height: 24px;
  }

  .cta {
    position: absolute;
    left: 692px;
    top: 287px;
    width: 345px;
    height: 67px;
    border-radius: 6px;
    background: linear-gradient(180deg, #62e055 0%, var(--green-dark) 100%);
    box-shadow: 0 2px 0 rgba(0,0,0,0.18);
    display: flex;
    align-items: center;
    padding-left: 26px;
    font-weight: 700;
    font-size: 20px;
    color: var(--white);
    text-decoration: none;
  }

  .price-band { position: absolute; left: 0; top: 0; }
  .price-line {
    position: absolute;
    left: 692px;
    top: 387px;
    font-weight: 700;
    font-size: 21px;
    line-height: 26px;
  }
  .price-line .accent { color: var(--green); }

  .categories {
    position: absolute;
    top: 470px;
    left: 0;
    width: 100%;
    list-style: none;
    font-weight: 500;
    font-size: 17.5px;
    line-height: 24px;
  }
  .categories li { position: absolute; white-space: nowrap; }

  .category-tab { position: absolute; left: 0; bottom: 0; }
  .tab-label {
    position: absolute;
    left: 283px;
    width: 607px;
    top: 522px;
    text-align: center;
    font-weight: 700;
    font-size: 20px;
    line-height: 26px;
    color: var(--tab-text);
  }
</style>
</head>
<body>
<main class="banner">

  <svg class="light-streaks" width="1200" height="560" viewBox="0 0 1200 560" aria-hidden="true">
    <defs>
      <linearGradient id="streakFade" x1="0" x2="1">
        <stop offset="0" stop-color="#5fd3ff" stop-opacity="0"/>
        <stop offset="0.4" stop-color="#5fd3ff" stop-opacity="0.7"/>
        <stop offset="1" stop-color="#5fd3ff" stop-opacity="0"/>
      </linearGradient>
    </defs>
    <path d="M0 378 C 160 360, 320 372, 520 400" stroke="url(#streakFade)" stroke-width="2" fill="none"/>
    <path d="M0 392 C 180 372, 340 384, 540 412" stroke="url(#streakFade)" stroke-width="1.2" fill="none" opacity="0.7"/>
    <path d="M20 410 C 200 392, 360 400, 560 430" stroke="url(#streakFade)" stroke-width="1" fill="none" opacity="0.5"/>
    <ellipse cx="360" cy="410" rx="320" ry="26" fill="#3fb6ff" opacity="0.12"/>
  </svg>

  <h1 class="headline">INCREASE <span class="accent">LEADS AND SALES</span> OVERNIGHT</h1>

  <svg class="flyer-stack" width="640" height="470" viewBox="0 0 640 470" role="img"
       aria-label="Fanned stack of printed incentive certificates: smart tablet, Las Vegas stay, dining voucher, cruise and luxury resort getaway">
    <defs>
      <linearGradient id="flyerSea" x1="0" y1="0" x2="0" y2="1">
        <stop offset="0" stop-color="#2f6fc4"/>
        <stop offset="0.35" stop-color="#6fa8d8"/>
        <stop offset="0.5" stop-color="#f2f2f2"/>
        <stop offset="1" stop-color="#e6e6e6"/>
      </linearGradient>
      <linearGradient id="flyerWarm" x1="0" y1="0" x2="0" y2="1">
        <stop offset="0" stop-color="#2a2a2a"/>
        <stop offset="0.35" stop-color="#8a3b22"/>
        <stop offset="0.5" stop-color="#f2f2f2"/>
        <stop offset="1" stop-color="#e4e4e4"/>
      </linearGradient>
    </defs>
    <polygon points="140,157 200,150 200,353 140,359" fill="url(#flyerWarm)" opacity="0.9"/>
    <polygon points="193,140 253,127 253,367 193,370" fill="url(#flyerWarm)"/>
    <polygon points="248,121 320,107 320,393 248,395" fill="url(#flyerWarm)"/>
    <polygon points="313,105 400,93 400,417 313,417" fill="url(#flyerSea)"/>
    <polygon points="397,95 619,107 619,405 397,460" fill="url(#flyerSea)"/>
  </svg>

  <p class="pitch">Create exciting marketing promotions giving away smart devices, vacation certificates, dining vouchers and other incentives to your customers</p>

  <a class="cta" href="https://www.brightlanepromoworks.biz/incentives">Get A Free Sample Package</a>

  <svg class="price-band" width="1200" height="560" viewBox="0 0 1200 560" aria-hidden="true">
    <defs>
      <linearGradient id="bandFill" x1="0" x2="1">
        <stop offset="0" stop-color="#0f67b8" stop-opacity="0.4"/>
        <stop offset="0.3" stop-color="#1277cf"/>
        <stop offset="1" stop-color="#0f6cc0"/>
      </linearGradient>
    </defs>
    <polygon points="665,383 1200,383 1200,417 640,417" fill="url(#bandFill)"/>
    <line x1="665" y1="383" x2="1200" y2="383" stroke="#39b4f5" stroke-width="1.5"/>
    <line x1="640" y1="417" x2="1200" y2="417" stroke="#39b4f5" stroke-width="1.5"/>
  </svg>
  <p class="price-line">Unlimited Incentives <span class="accent">Only $99/mth</span></p>

  <ul class="categories">
    <li style="left:128px">VACATION</li>
    <li style="left:257px">CRUISE</li>
    <li style="left:357px">RESORT</li>
    <li style="left:461px">DINING &amp; RESTAURANT</li>
    <li style="left:695px">SMART DEVICE</li>
    <li style="left:865px">DISCOUNTS SAVINGS</li>
  </ul>

  <svg class="category-tab" width="1200" height="50" viewBox="0 0 1200 50" aria-hidden="true">
    <defs>
      <linearGradient id="tabFill" x1="0" y1="0" x2="0" y2="1">
        <stop offset="0" stop-color="#ffffff"/>
        <stop offset="1" stop-color="#d7dde4"/>
      </linearGradient>
    </defs>
    <path d="M283 50 L300 10 Q303 4 310 4 L862 4 Q869 4 872 10 L890 50 Z" fill="url(#tabFill)"/>
  </svg>
  <p class="tab-label">CERTIFICATES, VOUCHERS &amp; INCENTIVES</p>

</main>
</body>
</html>
```